elegant beautiful Hang tag for a novelty makeup towel

It's a black hand towel in the shape of a little black dress. it is called VELVET EVENING CLOTH, it is a CLEAN SLATE FACE CLOTH. (doesn't show our makeup stains) Made in USA

Target Market(s)

ALL Women , Makeup artists, novelty THIS WILL BE IN THE HALVERDALE STORES AND PRESCOTWICK STORES.

Industry/Entity Type

Makeup

Contact Information for Business Card

I actually need a hang tag for a homemade handmade towel. I have a logo that I want on the tag and know what we want to say on it, on back needs to say "The essential to every girl's wardrobe. So when the little black dress comes off, our VELVET EVENING CLOTH is there to help you wash your day away. Include website www.velveteveningcloth.example OH INCLUDE TM (trademark sign next to logo please. Also, in small print on back from the makers of THE ORIGINAL CLEAN SLATE FACE CLOTH. handmade in USA. also CLEAN SLATE FACE CLOTH IN big font on front under logo sign with light colored pink lips after 'NO SHOW" but have no idea about fonts, graphics, placement or design. Want it classy, elegant, girly! COLORS LIGHT BEIGER BACKGROUND WITH BLACK WRITING/ DESIGNS

Font styles to use
Serif
Decorative
Script

Colors
fff3d1

Requirements
Must have
• Black cream girly , also state in big writing that it's a " clean slate face cloth" with a tiny light pink lip between the show and makeup. Include www.velveteveningcloth.example Quillfern Goods, LLC
Nice to have
• Perhaps an outline of a little black dress. A black scroll edge of some sort around card. Classy

```html
<!DOCTYPE html>
<html lang="en">
<head>
<meta charset="utf-8">
<title>Velvet Evening Cloth – Hang Tag</title>
<link rel="stylesheet" href="https://fonts.googleapis.com/css2?family=Josefin+Sans:wght@400;600&family=Didact+Gothic&family=Arimo:ital,wght@1,700&family=Open+Sans:wght@400&family=Poiret+One&display=swap">
<style>
  :root {
    --cream: #fff9d0;
    --tag-cream: #fff8d6;
    --ink: #000000;
    --paper-text: #f4efd9;
    --pink: #f29af0;
    --pink-line: #f7b4d8;
    --peach: #f6c89a;
    --peach-soft: #fbe3bf;
  }
  * { box-sizing: border-box; margin: 0; padding: 0; }
  html, body { width: 1200px; height: 1047px; overflow: hidden; }
  body { background: var(--cream); position: relative; font-family: "Didact Gothic", sans-serif; }

  .tag { position: absolute; width: 413px; height: 686px; top: 199px; }
  .tag--front { left: 137px; background: var(--tag-cream); }
  .tag--back { left: 655px; background: var(--ink); }

  .brand-name {
    font-family: "Poiret One", sans-serif;
    color: var(--paper-text);
    font-size: 19px;
    letter-spacing: 3px;
    text-align: center;
    position: absolute; left: 0; right: 0;
    display: flex; align-items: center; justify-content: center; gap: 8px;
  }
  .brand-name .tm { font-size: 10px; letter-spacing: 0; align-self: flex-start; }

  .tag__header { position: absolute; top: 0; left: 0; width: 100%; height: 162px; background: var(--ink); }
  .tag__header .brand-name { top: 70px; }
  .tag__rule { position: absolute; top: 164px; left: 0; width: 100%; height: 2px; background: var(--pink-line); }

  .tag__wash {
    position: absolute; top: 166px; left: 0; width: 100%; height: 402px;
    background:
      radial-gradient(ellipse 60% 55% at 35% 35%, var(--peach) 0%, rgba(246,200,154,0.55) 55%, rgba(246,200,154,0) 100%),
      radial-gradient(ellipse 70% 50% at 70% 85%, var(--peach-soft) 0%, rgba(251,227,191,0) 100%);
  }

  .product-title { position: absolute; top: 262px; left: 0; width: 100%; text-align: center; font-family: "Josefin Sans", sans-serif; color: var(--ink); }
  .product-title__lead { display: block; font-size: 28px; font-weight: 400; letter-spacing: 0.5px; line-height: 1; }
  .product-title__accent { color: var(--pink); }
  .product-title__main { display: block; font-size: 66px; font-weight: 600; letter-spacing: 1px; line-height: 1; margin-top: 6px; }

  .makers { position: absolute; left: 0; width: 100%; text-align: center; color: var(--ink); }
  .makers__intro { font-size: 13px; }
  .makers__name { font-size: 13px; margin-top: 4px; }
  .tag--front .makers { top: 393px; }
  .made-in { position: absolute; top: 438px; left: 0; width: 100%; text-align: center; font-family: "Arimo", sans-serif; font-style: italic; font-weight: 700; font-size: 20px; color: var(--ink); }

  .tag__web { position: absolute; top: 568px; left: 0; width: 100%; height: 47px; background: var(--ink); color: var(--paper-text); font-family: "Open Sans", sans-serif; font-size: 17px; display: flex; align-items: center; justify-content: center; }

  .tag--back .brand-name { top: 318px; }
  .tag--back .makers { top: 578px; color: var(--paper-text); }
</style>
</head>
<body>
  <section class="tag tag--front">
    <header class="tag__header">
      <div class="brand-name">VELVET EVENING CLOTH<span class="tm">™</span></div>
    </header>
    <div class="tag__rule"></div>
    <div class="tag__wash" role="img" aria-label="Soft peach watercolour wash"></div>
    <h1 class="product-title">
      <span class="product-title__lead">CLEAN SLATE <span class="product-title__accent">FACE</span></span>
      <span class="product-title__main">CLOTH</span>
    </h1>
    <div class="makers">
      <p class="makers__intro">from the makers of</p>
      <p class="makers__name">THE ORIGINAL CLEAN SLATE FACE CLOTH</p>
    </div>
    <p class="made-in">handmade in USA</p>
    <footer class="tag__web">www.velveteveningcloth.example</footer>
  </section>

  <section class="tag tag--back">
    <div class="brand-name">VELVET EVENING CLOTH<span class="tm">™</span></div>
    <div class="makers">
      <p class="makers__intro">from the makers of</p>
      <p class="makers__name">THE ORIGINAL CLEAN SLATE FACE CLOTH</p>
    </div>
  </section>
</body>
</html>
```